Threads of Kindness needs a new flyer fast for a giveaway

I am running a contest for the month of December. The woman selected as the winner of the contest will be someone that that has survived a domestic violence situation but would like to kick start in her new life journey. The winner selected will receive 1 month free personal training with a fitness coach 3 times a week, 4 week delivery of smoothies from Leafwhirl and a style consultation and outfit by Celebrity Stylist R.Tasker. All interested candidates should submit a brief personal bio including the reason they should be selected. Submissions are due December 24th and the winner will be selected December 31. Submissions should be sent to threadsofkindnessdallas@maildrop-example.net

Industry/Entity Type

Fashion

Font styles to use
Serif

Colors
886aae
b7a5cd
e4daeb
d2a4cc
b768aa
a64599
e34197
e667a6
eea4c8

Requirements
Must have
• The project has to be worded in a stylish way. I want it is be creative and eye catchy. It also needs to have my threads of kindness logo and my Ada V logo on the flyer that I will attach to the brief
Nice to have
• I would like to see different fonts to break up the flyer
Should not have
• It should not just be a paragraph of what I already typed about the contest

```html
<!DOCTYPE html>
<html lang="en">
<head>
<meta charset="utf-8">
<title>Threads of Kindness – December Giveaway Flyer</title>
<link rel="stylesheet" href="https://fonts.googleapis.com/css2?family=PT+Sans+Narrow:wght@400;700&family=Open+Sans:ital,wght@0,600;1,700&display=swap">
<style>
  :root {
    --stage: #dcdcde;
    --ink: #0f0b0d;
    --white: #ffffff;
    --pink: #e34197;
    --pink-soft: #e667a6;
    --magenta: #a64599;
    --orchid: #b768aa;
    --violet: #886aae;
    --lilac: #b7a5cd;
  }
  * { box-sizing: border-box; margin: 0; padding: 0; }
  html, body { width: 1200px; height: 1200px; overflow: hidden; background: var(--stage); }
  .canvas { position: relative; width: 1200px; height: 1200px; }
  .flyer {
    position: absolute; left: 149px; top: 20px;
    width: 962px; height: 1237px;
    transform: scale(0.9378); transform-origin: top left;
    background: var(--ink); overflow: hidden;
    font-family: "PT Sans Narrow", "Arial Narrow", sans-serif;
    color: var(--white);
  }
  .hero-photo {
    position: absolute; left: 0; top: 0; width: 962px; height: 880px;
    background:
      radial-gradient(ellipse 260px 360px at 780px 240px, rgba(166,69,153,.95), transparent 75%),
      radial-gradient(ellipse 200px 280px at 420px 260px, rgba(210,164,204,.55), transparent 75%),
      radial-gradient(ellipse 180px 160px at 280px 80px, rgba(120,70,90,.6), transparent 80%),
      linear-gradient(180deg, #3a1b33 0%, #5a2451 40%, #2a1226 75%, var(--ink) 100%);
  }
  .intro {
    position: absolute; left: 66px; top: 240px; width: 320px;
    font-size: 19.5px; line-height: 27.5px; font-weight: 400;
  }
  .intro strong { font-weight: 700; }
  .headline {
    position: absolute; left: 58px; top: 392px;
    font-weight: 700; text-transform: uppercase; line-height: 1;
  }
  .headline .lead { display: block; font-size: 64px; letter-spacing: -0.5px; }
  .headline .main { display: block; font-size: 96px; margin-top: 6px; letter-spacing: -1px; }
  .band {
    position: absolute; left: 0; top: 562px; width: 962px; height: 73px;
    background: var(--pink);
  }
  .band h2 {
    position: absolute; left: 62px; top: 4px;
    font-size: 56px; font-weight: 700; text-transform: uppercase; letter-spacing: -0.3px; line-height: 64px;
  }
  .summary {
    position: absolute; left: 64px; top: 662px; width: 820px;
    font-size: 27px; line-height: 35px; font-weight: 700;
  }
  .prize { position: absolute; left: 64px; top: 808px; width: 420px; }
  .prize h3 {
    font-family: "Open Sans", Verdana, sans-serif; font-weight: 600;
    font-size: 24px; color: var(--pink); line-height: 30px;
  }
  .prize p {
    font-family: "Open Sans", Verdana, sans-serif; font-style: italic; font-weight: 700;
    font-size: 17px; line-height: 24px;
  }
  .prize .stylist { display: block; font-size: 23px; line-height: 34px; }
  .how-to {
    position: absolute; left: 534px; top: 808px; width: 360px;
    font-size: 21.5px; line-height: 27.5px; font-weight: 700;
  }
  .how-to p + p { margin-top: 27px; }
  .edge-strip {
    position: absolute; left: 0; top: 1029px; width: 44px; height: 118px; background: var(--pink);
  }
  .brand-row { position: absolute; left: 66px; top: 1029px; height: 118px; display: flex; align-items: center; }
  .brand-name {
    font-family: "PT Sans Narrow", "Arial Narrow", sans-serif; font-weight: 700;
    font-size: 30px; line-height: 32px; color: var(--pink);
  }
  .brand-name.secondary { color: var(--lilac); font-size: 44px; }
  .brand-divider { width: 1px; height: 104px; background: #5a2a4a; margin: 0 24px; }
  .contact {
    position: absolute; left: 518px; top: 1029px; width: 444px; height: 118px;
    background: var(--pink); padding: 12px 24px; color: var(--ink);
  }
  .contact h4 { font-size: 23px; font-weight: 700; text-transform: uppercase; line-height: 26px; }
  .contact ul { list-style: none; display: flex; gap: 13px; margin-top: 6px; padding-left: 4px; }
  .contact li { font-family: "Open Sans", Verdana, sans-serif; font-weight: 600; font-size: 13.5px; }
</style>
</head>
<body>
<main class="canvas">
  <article class="flyer">
    <div class="hero-photo" role="img" aria-label="Blurred photo of a frightened woman behind a raised clenched fist, tinted in magenta"></div>

    <p class="intro">A non profit that host <strong>FASHION SHOWS</strong> to raise awareness and funds for domestic violence survivors.</p>

    <h1 class="headline">
      <span class="lead">Are you victim of</span>
      <span class="main">Domestic Violence ?</span>
    </h1>

    <div class="band"><h2>Like to kick start new life journey</h2></div>

    <p class="summary">We are &nbsp;running a contest for the month of December to a woman that has survived a domestic violence situation but would like to kick start in her new life journey.</p>

    <section class="prize">
      <h3>The winner selected will receive</h3>
      <p>1 month free personal training with a fitness coach 3 times a week, 4 week delivery of smoothies from Leafwhirl and a style consultation and outfit by Celebrity Stylist <span class="stylist">R.Tasker.</span></p>
    </section>

    <section class="how-to">
      <p>All interested should submit a brief personal bio including the reason you should be selected.</p>
      <p>Submissions are due December 24th and the winner will be selected December 31.</p>
    </section>

    <div class="edge-strip"></div>
    <div class="brand-row">
      <span class="brand-name">Threads of<br>Kindness</span>
      <span class="brand-divider"></span>
      <span class="brand-name secondary">Ada V</span>
    </div>

    <section class="contact">
      <h4>Contact us</h4>
      <ul>
        <li>NEED DETAILS</li>
        <li>NEED DETAILS</li>
        <li>NEED DETAILS</li>
      </ul>
    </section>
  </article>
</main>
</body>
</html>
```